Torvane PT Business Card

I need the card to be bright/bold colours to stand out amongst others.
It needs to have my company logo.
I was not interested in pictures etc just a layout that attracts attention.

I have attached my old design which is very plain. I also needed change the contact details. And my description changed to Personal Trainer
Phone 0427391058
Facebook Torvane PT
No email address please, no street address.
And only Torvane PT (Please remove anything to do with Torvane Supplements)

```html
<!DOCTYPE html>
<html lang="en">
<head>
<meta charset="utf-8">
<title>Torvane PT Business Card</title>
<link rel="stylesheet" href="https://fonts.googleapis.com/css2?family=Saira:wght@400;600;800&display=swap">
<style>
  :root {
    --stage: #5a5a5a;
    --card: #ffffff;
    --brand-blue: #1478c8;
    --brand-blue-light: #1b93d4;
    --brand-yellow: #ffdc14;
    --text-grey: #4a4a4a;
    --on-blue: #ffffff;
  }
  html, body {
    margin: 0;
    width: 1200px;
    height: 900px;
    overflow: hidden;
    background: var(--stage);
  }
  .business-card {
    position: absolute;
    left: 100px;
    top: 170px;
    width: 1000px;
    height: 560px;
    border-radius: 44px;
    background: var(--card);
    overflow: hidden;
    font-family: "Saira", sans-serif;
  }
  .card-shapes {
    position: absolute;
    inset: 0;
  }
  .brand-name {
    position: absolute;
    left: 78px;
    top: 112px;
    margin: 0;
    font-size: 70px;
    font-weight: 800;
    line-height: 1;
    letter-spacing: 1px;
    color: var(--brand-blue);
  }
  .brand-rule {
    position: absolute;
    left: 110px;
    top: 206px;
    width: 330px;
    height: 2px;
    background: var(--brand-blue);
  }
  .person {
    position: absolute;
    left: 150px;
    top: 262px;
    text-align: left;
  }
  .person-name {
    margin: 0;
    font-size: 40px;
    font-weight: 600;
    line-height: 1;
    color: var(--brand-blue);
    letter-spacing: 1px;
  }
  .person-role {
    margin: 6px 0 0 0;
    font-size: 24px;
    font-weight: 400;
    line-height: 1;
    color: var(--text-grey);
    letter-spacing: 1px;
  }
  .contact-list {
    position: absolute;
    right: 58px;
    top: 300px;
    margin: 0;
    padding: 0;
    list-style: none;
    color: var(--on-blue);
    font-size: 26px;
    font-weight: 400;
  }
  .contact-item {
    display: flex;
    justify-content: flex-end;
    align-items: center;
    gap: 14px;
    height: 38px;
  }
  .contact-item + .contact-item { margin-top: 6px; margin-right: -26px; }
  .contact-icon {
    width: 26px;
    height: 26px;
    border-radius: 5px;
    background: var(--on-blue);
    display: flex;
    align-items: center;
    justify-content: center;
  }
</style>
</head>
<body>
  <main class="business-card">
    <svg class="card-shapes" width="1000" height="560" viewBox="0 0 1000 560" aria-hidden="true">
      <defs>
        <linearGradient id="blueSweep" x1="1" y1="0" x2="0" y2="1">
          <stop offset="0" stop-color="#1580cc"/>
          <stop offset="0.5" stop-color="#1b93d4"/>
          <stop offset="1" stop-color="#1272c4"/>
        </linearGradient>
      </defs>
      <path class="accent-stripe" fill="var(--brand-yellow)"
            d="M0,418 C420,420 700,320 820,190 C750,340 470,452 0,452 Z"/>
      <path class="blue-panel" fill="url(#blueSweep)"
            d="M905,0 C860,300 520,468 0,470 L0,560 L1000,560 L1000,0 Z"/>
    </svg>

    <h1 class="brand-name">TORVANE PT</h1>
    <div class="brand-rule"></div>

    <section class="person">
      <p class="person-name">DANA MERCER</p>
      <p class="person-role">PERSONAL TRAINER</p>
    </section>

    <ul class="contact-list">
      <li class="contact-item">
        <span>0427391058</span>
        <span class="contact-icon">
          <svg width="18" height="18" viewBox="0 0 24 24" aria-hidden="true">
            <path fill="var(--brand-blue)" d="M6.6 10.8a15.1 15.1 0 0 0 6.6 6.6l2.2-2.2a1 1 0 0 1 1-.25 11.4 11.4 0 0 0 3.6.57 1 1 0 0 1 1 1V20a1 1 0 0 1-1 1A17 17 0 0 1 3 4a1 1 0 0 1 1-1h3.5a1 1 0 0 1 1 1c0 1.25.2 2.45.57 3.57a1 1 0 0 1-.25 1z"/>
          </svg>
        </span>
      </li>
      <li class="contact-item">
        <span>Torvane PT</span>
        <span class="contact-icon"></span>
      </li>
    </ul>
  </main>
</body>
</html>
```